Byte Crew - Settle In

A flyer to promote a service by Byte Crew that provides IT set up in home when moving house.

It should be for print format (A4, A5 and an email friendly version)

Logos, previous flyer, image all attached.

Please use black, green and white as base colours.Please change boys sweater/jumper in the photo to green to match the logo.

Byte Crew are bring a helpdesk to your front door, saving you time and money. With a variety of packages to suit your needs, the Byte Crew aims to tackle both small and complex issues from setting up a home network to servicing the needs of a growing company.

Target Market(s)

Consumers moving house, Relocation agents, Real Estate agents

Requirements
Must have
• Logo, image, text all attached
• Use of green, black and white
Nice to have
• Also have coloured ties if you want them for design

```html
<!DOCTYPE html>
<html lang="en">
<head>
<meta charset="utf-8">
<title>Byte Crew – Settle In</title>
<link rel="stylesheet" href="https://fonts.googleapis.com/css2?family=Anton&family=Arimo:ital,wght@0,400;0,700;1,400&display=swap">
<style>
  :root {
    --green: #8cc63f;
    --black: #231f20;
    --white: #ffffff;
    --light-grey: #ececec;
    --ink: #1a1a1a;
    --photo-dark: #2e3a2a;
    --photo-mid: #5d6b52;
    --photo-light: #a9b4a0;
  }
  * { box-sizing: border-box; margin: 0; padding: 0; }
  html, body { width: 880px; height: 1200px; overflow: hidden; background: var(--white); }
  .flyer {
    position: relative; width: 880px; height: 1200px; overflow: hidden;
    font-family: "Arimo", Arial, sans-serif; color: var(--ink);
  }
  .hero-photo {
    position: absolute; left: 0; top: 0; width: 880px; height: 558px;
    background:
      radial-gradient(ellipse 420px 360px at 600px 240px, var(--photo-light) 0%, var(--photo-mid) 55%, transparent 80%),
      linear-gradient(160deg, var(--photo-mid) 0%, var(--photo-dark) 100%);
  }
  .hero-question {
    position: absolute; left: 37px; top: 54px; width: 330px; height: 210px;
    background: rgba(255,255,255,0.85);
    padding: 16px 0 0 12px;
    font-family: "Anton", Impact, sans-serif; color: var(--black);
    font-size: 44px; line-height: 1.2;
  }
  .hero-question .emphasis { font-size: 72px; line-height: 0.9; }
  .tagline-band {
    position: absolute; left: 0; top: 558px; width: 880px; height: 84px;
    background: var(--green);
    font-family: "Anton", Impact, sans-serif; font-size: 52px; color: var(--black);
  }
  .tagline-band .lead { position: absolute; left: 28px; top: 4px; }
  .tagline-band .tail { position: absolute; right: 28px; top: 4px; }
  .brand-box {
    position: absolute; left: 392px; top: 516px; width: 274px; height: 166px;
    background: var(--white);
    display: flex; align-items: center; justify-content: center; gap: 12px;
    font-family: "Anton", Impact, sans-serif; font-size: 42px; color: var(--black);
  }
  .brand-box .mark { width: 16px; height: 16px; background: var(--green); }
  .intro-panel {
    position: absolute; left: 0; top: 642px; width: 880px; height: 164px;
    background: var(--black);
  }
  .intro-copy {
    position: absolute; left: 70px; top: 20px; width: 350px;
    color: var(--white); font-weight: 700; font-size: 18px; line-height: 1.3; text-align: center;
  }
  .offer-title {
    position: absolute; left: 440px; top: 42px; width: 360px;
    font-family: "Anton", Impact, sans-serif; color: var(--green);
    font-size: 50px; line-height: 1.0; text-align: center; letter-spacing: 1px;
  }
  .pointer { position: absolute; left: 170px; top: 764px; width: 76px; height: 66px; }
  .inclusions {
    position: absolute; left: 0; top: 806px; width: 880px; height: 274px;
    background: var(--light-grey);
    padding: 42px 30px 0 56px;
  }
  .inclusions ul { list-style: none; font-size: 15.5px; line-height: 22.5px; }
  .inclusions li { position: relative; padding-left: 36px; }
  .inclusions li::before { content: "•"; position: absolute; left: 0; }
  .inclusions .footnotes { margin-top: 6px; font-style: italic; font-size: 15px; line-height: 20px; }
  .booking-strip { position: absolute; left: 0; top: 1080px; width: 880px; height: 120px; }
  .booking-strip svg { position: absolute; inset: 0; }
  .book-now {
    position: absolute; left: 22px; top: 26px;
    font-family: "Anton", Impact, sans-serif; font-size: 60px; color: var(--black);
  }
  .contact {
    position: absolute; left: 420px; top: 12px; width: 400px; text-align: center;
    color: var(--green); font-weight: 700; font-size: 24px; line-height: 32px;
  }
</style>
</head>
<body>
<main class="flyer">
  <div class="hero-photo" role="img" aria-label="Photo of a startled boy in glasses and a green jumper holding two unplugged cables"></div>
  <div class="hero-question">Can’t remember<br>what to <span class="emphasis">plug</span><br>in where?</div>

  <div class="tagline-band">
    <span class="lead">Do not fear, the</span>
    <span class="tail">is here!</span>
  </div>
  <div class="brand-box"><span class="mark"></span><span>Byte Crew</span></div>

  <section class="intro-panel">
    <p class="intro-copy">We take all the pain out of moving house and get you set-up, online and connected before you can say the word Geek.</p>
    <h1 class="offer-title">SETTLE IN<br>GEEK $425</h1>
  </section>

  <section class="inclusions">
    <ul>
      <li>Pre-visit online assessment to ensure maximum use of our Geek’s time</li>
      <li>Ready:&nbsp; IT Health Check and Audit report</li>
      <li>Set:&nbsp; Connection of your wireless network for user access including passwords and parental control if desired</li>
      <li>Go: Set up of 3 computers and 1 printer</li>
      <li>Expanding the family: Connection of one additional device eg media box, tablet, games console, Smart TV*</li>
      <li>Updating of software and virus security check</li>
      <li>Byte Crew Membership</li>
      <li>Includes travel cost and up to 4 hours of a Geek’s time in your house</li>
      <li>1 month free on Crew@Home Packages**</li>
      <li>Awesome Byte Crew fridge magnet</li>
    </ul>
    <p class="footnotes">*Each additional device set-up is charged at $35<br>** Based on our annual packages and If signed within 14 days</p>
  </section>

  <svg class="pointer" viewBox="0 0 76 66" aria-hidden="true"><polygon points="0,0 76,0 38,66" fill="var(--green)"/></svg>

  <footer class="booking-strip">
    <svg viewBox="0 0 880 120" preserveAspectRatio="none" aria-hidden="true">
      <rect width="880" height="120" fill="var(--green)"/>
      <path d="M880 0 H420 Q380 0 372 40 L352 120 H880 Z" fill="var(--black)"/>
    </svg>
    <div class="book-now">Book Now!</div>
    <div class="contact">www.bytecrew.asia<br>Email: booking@bytecrew.asia<br>Hotline: 6612 3408</div>
  </footer>
</main>
</body>
</html>
```